Design für 3-Monatskalender
Zielgruppe
Hallo, wir benötigen ein Design bzw. fertige Druckdaten für einen 3 Monatskalender mit den Feiertagen aus DE, AT und CH.
Format ist DIN A6, der Kalender wird benötigt für das Jahr 2024 und 2025.
Aufgabenstellung
Format: DIN A6
Kalendarium 2024 und 2025
Feiertage aus DE, AT und CH
Beispiel anbei, wichtig ist, das wir einen Magnetischen Ring als Datumsschieber nehmen. Der Ring hat die Maße: Durchmesser = 12mm Innendruchmesser = 10mm

```html
<!DOCTYPE html>
<html lang="de">
<head>
<meta charset="utf-8">
<title>3-Monatskalender 2024</title>
<link href="https://fonts.googleapis.com/css2?family=Rubik:wght@300;500;700&display=swap" rel="stylesheet">
<style>
  :root {
    --paper: #ffffff;
    --frame: #a4a4a4;
    --band: #c6c6c6;
    --band-text: #ffffff;
    --ink: #222222;
    --week: #a0a0a0;
    --ring: #9c9c9c;
  }
  * { margin: 0; padding: 0; box-sizing: border-box; }
  html, body {
    width: 1200px; height: 1200px; overflow: hidden;
    background: var(--paper);
    font-family: "Rubik", sans-serif;
    color: var(--ink);
  }
  .calendar-card {
    position: absolute; left: 246px; top: 101px;
    width: 706px; height: 997px;
    border: 3px solid var(--frame);
  }
  .month { position: absolute; left: 279px; width: 638px; }
  .month-title {
    position: absolute; left: 0; top: -48px; width: 678px; height: 36px;
    text-align: center; font-weight: 700; font-size: 35px; line-height: 36px;
    letter-spacing: 1.5px;
  }
  .weekday-band {
    display: grid; grid-template-columns: 40px repeat(7, 1fr);
    height: 19px; background: var(--band);
  }
  .weekday-band span {
    color: var(--band-text); font-weight: 500; font-size: 14px;
    line-height: 19px; text-align: center;
  }
  .days {
    display: grid; grid-template-columns: 40px repeat(7, 1fr);
    grid-auto-rows: 47px; padding-top: 0.5px;
  }
  .days span {
    font-weight: 300; font-size: 38px; line-height: 47px; text-align: center;
  }
  .days .week {
    grid-column: 1; font-size: 16px; font-weight: 500; color: var(--week);
    line-height: 43px;
  }
  .holidays {
    position: absolute; font-size: 13px; font-weight: 300; line-height: 17px;
    white-space: nowrap; text-align: left;
  }
  .holidays b { font-weight: 500; }
  .holidays-jan { left: 306px; top: 212px; }
  .holidays-mar { left: 162px; top: 40px; }
  .date-ring {
    position: absolute; left: 580px; top: 496px; width: 80px; height: 80px;
  }
</style>
</head>
<body>
  <div class="calendar-card"></div>

  <section class="month" style="top:176px">
    <h2 class="month-title">JANUAR 2024</h2>
    <div class="weekday-band"><span></span><span>Mo</span><span>Di</span><span>Mi</span><span>Do</span><span>Fr</span><span>Sa</span><span>So</span></div>
    <div class="days">
      <span class="week">1</span><span>1</span><span>2</span><span>3</span><span>4</span><span>5</span><span>6</span><span>7</span>
      <span class="week">2</span><span>8</span><span>9</span><span>10</span><span>11</span><span>12</span><span>13</span><span>14</span>
      <span class="week">3</span><span>15</span><span>16</span><span>17</span><span>18</span><span>19</span><span>20</span><span>21</span>
      <span class="week">4</span><span>22</span><span>23</span><span>24</span><span>25</span><span>26</span><span>27</span><span>28</span>
      <span class="week">5</span><span>29</span><span>30</span><span>31</span>
    </div>
    <p class="holidays holidays-jan"><b>Feiertage:</b> 1. 1. Neujahr (D, A, CH), 2. 1. Berchtoldstag<br>(CH), 6. 1. Heilige Drei Könige (CH),</p>
  </section>

  <section class="month" style="top:493px">
    <h2 class="month-title">FEBRUAR 2024</h2>
    <div class="weekday-band"><span></span><span>Mo</span><span>Di</span><span>Mi</span><span>Do</span><span>Fr</span><span>Sa</span><span>So</span></div>
    <div class="days">
      <span class="week">5</span><span style="grid-column:5">1</span><span>2</span><span>3</span><span>4</span>
      <span class="week">6</span><span>5</span><span>6</span><span>7</span><span>8</span><span>9</span><span>10</span><span>11</span>
      <span class="week">7</span><span>12</span><span>13</span><span>14</span><span>15</span><span>16</span><span>17</span><span>18</span>
      <span class="week">8</span><span>19</span><span>20</span><span>21</span><span>22</span><span>23</span><span>24</span><span>25</span>
      <span class="week">9</span><span>26</span><span>27</span><span>28</span><span>29</span>
    </div>
  </section>

  <section class="month" style="top:810px">
    <h2 class="month-title">MÄRZ 2024</h2>
    <div class="weekday-band"><span></span><span>Mo</span><span>Di</span><span>Mi</span><span>Do</span><span>Fr</span><span>Sa</span><span>So</span></div>
    <div class="days">
      <span class="week">9</span><span style="grid-column:6">1</span><span>2</span><span>3</span>
      <span class="week">10</span><span>4</span><span>5</span><span>6</span><span>7</span><span>8</span><span>9</span><span>10</span>
      <span class="week">11</span><span>11</span><span>12</span><span>13</span><span>14</span><span>15</span><span>16</span><span>17</span>
      <span class="week">12</span><span>18</span><span>19</span><span>20</span><span>21</span><span>22</span><span>23</span><span>24</span>
      <span class="week">13</span><span>25</span><span>26</span><span>27</span><span>28</span><span>29</span><span>30</span><span>31</span>
    </div>
    <p class="holidays holidays-mar"><b>Feiertage:</b> 19. 3. Josefstag (A, CH)</p>
  </section>

  <svg class="date-ring" viewBox="0 0 80 80" aria-hidden="true">
    <circle cx="40" cy="40" r="35" fill="none" stroke="var(--ring)" stroke-width="5.5"/>
  </svg>
</body>
</html>
```